Poster for List of Company Values

We need a poster to outline our Values which will be displayed in our office as well as posted on our website and other platforms (so need to allow for some flexibly in its application).

File attached outlines what we currently have with design and also our company style guide.

Note that we are looking for a modern, clean look, which still represents our core activities of construction and environmental services.

You can also reference our website here:

https://quorvelgroup.com.au/

Happy to answer any questions you might have.

Thanks for your interest,
Brent

Target Market(s)

Internal and External clients

Industry/Entity Type

Construction, water and recycling

Font styles to use
Sans Serif

Requirements
Must have
• All values on the one page. Graphic to represent each value. Also needs to use company logo
Nice to have
• Preference for poster to be orientated in landscape
Should not have
• Do not follow example provided, this is only to demonstrate what we have to date and also the text required

```html
<!DOCTYPE html>
<html lang="en">
<head>
<meta charset="utf-8">
<title>Quorvel Group — Our Values</title>
<link rel="stylesheet" href="https://fonts.googleapis.com/css2?family=Montserrat:wght@200;800&family=Open+Sans:ital,wght@0,700;1,600;1,700&display=swap">
<style>
  :root{
    --bg:#2a2829;
    --white:#ffffff;
    --loyal:#3eae97;
    --initiative:#56a83f;
    --team:#233f86;
    --respect:#c72b4a;
    --open:#e8884a;
    --positive:#dcc65c;
  }
  html,body{margin:0;padding:0;overflow:hidden;}
  body{width:1200px;height:1200px;background:var(--bg);position:relative;}
  .value-card{position:absolute;width:268px;height:268px;overflow:hidden;color:var(--white);}
  .value-card.loyal{left:152px;top:314px;background:var(--loyal);}
  .value-card.initiative{left:466px;top:314px;background:var(--initiative);}
  .value-card.team{left:779px;top:314px;background:var(--team);}
  .value-card.respect{left:152px;top:617px;background:var(--respect);}
  .value-card.open{left:466px;top:617px;background:var(--open);}
  .value-card.positive{left:779px;top:617px;background:var(--positive);}

  .value-icon{position:absolute;right:14px;top:14px;width:36px;height:36px;fill:none;stroke:var(--white);stroke-width:2.5;stroke-linecap:round;stroke-linejoin:round;}

  .line{position:absolute;left:13px;margin:0;line-height:1;white-space:nowrap;font-family:'Montserrat',sans-serif;}
  .line.light{font-weight:200;letter-spacing:-0.01em;}
  .line.bold{font-weight:800;letter-spacing:-0.035em;}

  .card-footer{position:absolute;left:14px;right:10px;top:208px;display:flex;align-items:flex-start;gap:10px;}
  .brand-name{font-family:'Montserrat',sans-serif;font-weight:800;font-size:11px;color:var(--white);width:54px;flex:none;padding-top:3px;}
  .value-text{margin:0;font-family:'Open Sans',sans-serif;font-style:italic;font-weight:700;font-size:11.2px;line-height:14px;}
  .value-text.small{font-size:10.2px;line-height:12.6px;}
  .value-text.large{font-size:12.6px;line-height:16px;}
</style>
</head>
<body>

<section class="value-card loyal">
  <svg class="value-icon" viewBox="0 0 36 36" role="img" aria-label="Shield icon for loyalty">
    <path d="M18 3 L31 8 V17 C31 25 25 30 18 33 C11 30 5 25 5 17 V8 Z"/>
  </svg>
  <p class="line light" style="top:45px;font-size:72px;">BE</p>
  <p class="line bold" style="top:104px;font-size:73px;">LOYAL</p>
  <div class="card-footer">
    <span class="brand-name">Quorvel</span>
    <p class="value-text">We take care of our own and provide opportunities to listen and support each other.</p>
  </div>
</section>

<section class="value-card initiative">
  <svg class="value-icon" viewBox="0 0 36 36" role="img" aria-label="Arrow icon for initiative">
    <path d="M7 29 L29 7"/><path d="M14 7 H29 V22"/>
  </svg>
  <p class="line light" style="top:48px;font-size:33px;left:18px;">SHOW</p>
  <p class="line bold" style="top:74px;font-size:75px;left:16px;">INITIA</p>
  <p class="line bold" style="top:134px;font-size:75px;left:26px;">TIVE</p>
  <div class="card-footer" style="top:210px;">
    <span class="brand-name">Quorvel</span>
    <p class="value-text">We celebrate and recognize our own and encourage forward thinking.</p>
  </div>
</section>

<section class="value-card team">
  <svg class="value-icon" viewBox="0 0 36 36" role="img" aria-label="Three linked circles icon for teamwork">
    <circle cx="18" cy="10" r="6"/><circle cx="9" cy="25" r="6"/><circle cx="27" cy="25" r="6"/>
  </svg>
  <p class="line light" style="top:74px;font-size:42px;left:15px;">THINK</p>
  <p class="line bold" style="top:100px;font-size:82px;left:14px;">TEAM</p>
  <div class="card-footer">
    <span class="brand-name">Quorvel</span>
    <p class="value-text">We communicate effectively and work as a team by helping and supporting each other.</p>
  </div>
</section>

<section class="value-card respect">
  <svg class="value-icon" viewBox="0 0 36 36" role="img" aria-label="Overlapping circles icon for respect">
    <circle cx="13" cy="18" r="9"/><circle cx="23" cy="18" r="9"/>
  </svg>
  <p class="line light" style="top:22px;font-size:41px;left:16px;">SHOW</p>
  <p class="line bold" style="top:55px;font-size:88px;left:12px;">RES</p>
  <p class="line bold" style="top:120px;font-size:88px;left:12px;">PECT</p>
  <div class="card-footer" style="top:214px;">
    <span class="brand-name">Quorvel</span>
    <p class="value-text large">We value the diversity and opinions of all.</p>
  </div>
</section>

<section class="value-card open">
  <svg class="value-icon" viewBox="0 0 36 36" role="img" aria-label="Open door icon for openness">
    <path d="M6 32 V4 H26 V32"/><path d="M6 4 L18 9 V33 L6 32"/><path d="M3 32 H33"/>
  </svg>
  <p class="line light" style="top:28px;font-size:43px;left:10px;">BE</p>
  <p class="line bold" style="top:62px;font-size:59px;left:9px;">OPEN</p>
  <p class="line light" style="top:112px;font-size:43px;left:8px;">AND</p>
  <p class="line bold" style="top:146px;font-size:59px;left:9px;">HONEST</p>
  <div class="card-footer" style="top:213px;">
    <span class="brand-name">Quorvel</span>
    <p class="value-text small">We are clear and open with each other, and provide an approachable and friendly environment.</p>
  </div>
</section>

<section class="value-card positive">
  <svg class="value-icon" viewBox="0 0 36 36" role="img" aria-label="Sun icon for positivity">
    <circle cx="18" cy="18" r="7"/>
    <path d="M18 2 V6 M18 30 V34 M2 18 H6 M30 18 H34 M7 7 L10 10 M26 26 L29 29 M29 7 L26 10 M10 26 L7 29"/>
  </svg>
  <p class="line light" style="top:69px;font-size:43px;left:13px;">BE</p>
  <p class="line bold" style="top:109px;font-size:51px;left:12px;">POSITIVE</p>
  <div class="card-footer" style="top:212px;">
    <span class="brand-name">Quorvel</span>
    <p class="value-text small">SMILE : We are solutions focused and encourage a positive attitude turning a negative into a positive.</p>
  </div>
</section>

</body>
</html>
```